Wordpress Template for Biomed tech startup

Needed: A wordpress based site ready to go with custom logo and icons - all we would have to do is add text and pics
We are a Princeton based startup company. We are currently developing advanced prosthetics that will be commercial in the next few years - in the meantime, we would like to sell robotics kits to get students and adults interested in Science, Tech, Math, and Engineering.

Our company is called KelterLimb.

Our first few kits include:
- A Robotic Arm kit (DIY kit allows you to build a robotic hand that has 8 points of movement)
- Sensor Glove Kit (use in conjunction with the robotic hand to have it mimic the actions your hand does with the glove on - or use it for other tech applications)

Target Market(s)

Makers, DIY community, students, science oriented young adults, investors

Industry/Entity Type

It Company

Requirements
Must have
• -Ecommerce ability (a plugin like Trendora would suffice)

Detailed creative brief Below:

Background

There is no current website for KelterLimb. In order to drive the progression of the company, there must be a website that will provide potential customers, investors, and employees with information about the company and how it came to be. The website must allow for users to discover information about the company, the products that are made and how to go about purchasing products. We want the website to be sleek and simple to appeal to our audience of technology oriented “makers”.

Communications Objectives
The objectives of this website are:

Provide information about the products that KelterLimb has developed.
Provide an avenue for potential customers to connect with KelterLimb
Display why our products are great for makers and other people interested in robotic-type products.

Tactical Objectives
EXTERNAL: The tactical objective is to create an inviting tool to help past, present, and future customers understand our business and validate their decision in purchasing our products.

INTERNAL: Establish a compelling site that is attracting potential customers. The website will also be a tool I helping to attract potential employees to the company.

Target Audience
“Makers” who would be interested in purchasing our products and/or who would discuss our product with friends, co-workers, etc. who have similar interests. Potential future employees could also discover us through the website. Investors.

Tone and Manner
Innovative, Technological, Approachable, Fresh

Mandatories
Must include KelterLimb logo
Focal colors - Keep logo in mind

Mapping and Layout

Home Page:
• MANDATORIES:
• KelterLimb logo
• Slideshow with 5 pictures
• Facebook
• Twitter
• Video from YouTube or Vimeo

About Us

Founder backstory
History of how founder began his work and why
Story of KelterLimb Creation
How the company came to be and what it took to start it

Investors Page -Password protected "investors" page - if a potential investor doesnt have a password to this page they may fill out an e-form with their information (which should be emailed to a KelterLimb employee for approval) and they get the password to access after approval.

Prosthetic Hand

Info about the hand
Video of the hand working

Robotic Hand Kits

Info about the hand kit
Video/commercial of the hand
Option to purchase the kit

Glove Kits

Info about the hand kit

Contact Us

Contact information page for visitors to fill out a contact us form
Our Contact info as well

Nice to have
• Background and text similar to that of business card

```html
<!DOCTYPE html>
<html lang="en">
<head>
<meta charset="utf-8">
<title>KelterLimb</title>
<link href="https://fonts.googleapis.com/css2?family=PT+Sans:wght@400;700&family=Exo+2:wght@500;600&display=swap" rel="stylesheet">
<style>
:root{
  --blue-dark:#23507f;
  --blue:#2f6196;
  --blue-light:#4a7fb5;
  --heading:#2b5d8f;
  --text:#555;
  --text-dark:#222;
  --muted:#8a8a8a;
  --line:#e2e2e2;
  --page:#f7f7f7;
  --btn:#3a3a3a;
}
*{box-sizing:border-box;margin:0;padding:0}
html,body{width:1169px;height:1200px;overflow:hidden}
body{position:relative;background:var(--page);font-family:"PT Sans",Arial,sans-serif;color:var(--text)}
.topbar{position:absolute;left:0;top:0;width:1169px;height:120px;background:linear-gradient(180deg,#2a5a8d 0%,#3466a0 100%)}
.search{position:absolute;left:88px;top:29px;width:216px;height:36px;border-radius:18px;background:#244d7a;box-shadow:inset 0 2px 4px rgba(0,0,0,.35),0 1px 0 rgba(255,255,255,.2);color:#c9d7e6;font-size:14px;line-height:36px;padding-left:19px}
.search svg{position:absolute;right:16px;top:10px}
.brand{position:absolute;left:0;width:1169px;top:18px;text-align:center;color:#fff;font-size:48px;font-weight:400;letter-spacing:-1px}
.cart{position:absolute;left:895px;top:32px;width:105px;height:31px;background:#fff;border-radius:2px;color:var(--blue);font-weight:700;font-size:14px;line-height:31px;padding-left:42px}
.cart svg{position:absolute;left:10px;top:6px}
.social{position:absolute;top:32px;width:31px;height:31px;background:#fff;border-radius:2px}
.nav{position:absolute;left:88px;top:96px;width:994px;height:47px;background:#fff;display:flex;box-shadow:0 4px 8px rgba(0,0,0,.08)}
.nav a{display:block;height:47px;line-height:47px;padding:0 24px;font-size:15px;color:#555;text-decoration:none;border-right:1px solid var(--line);text-transform:uppercase}
.nav a:last-child{border-right:0;flex:1;text-align:center}
.nav a.active{color:var(--blue);background:linear-gradient(#fff,#f1f1f1)}
.hero{position:absolute;left:0;top:120px;width:1169px;height:330px;background:radial-gradient(ellipse at 70% 50%,#fafafa 0%,#e8e8e8 80%)}
.hero h1{position:absolute;left:125px;top:62px;font-family:"Exo 2",sans-serif;font-weight:600;font-size:25px;color:var(--heading)}
.hero p{position:absolute;left:125px;top:106px;width:502px;font-size:14px;line-height:24.4px;color:#444}
.btn{display:inline-block;background:linear-gradient(#4a4a4a,#2c2c2c);color:#fff;font-family:"Exo 2",sans-serif;font-weight:500;text-transform:uppercase;border-radius:2px;border:1px solid #222}
.hero .btn{position:absolute;left:125px;top:222px;height:41px;line-height:39px;font-size:18px;padding:0 44px 0 10px}
.hero .btn svg{position:absolute;right:9px;top:10px}
.dots{position:absolute;left:126px;top:296px;display:flex;gap:9px}
.dots span{width:14px;height:14px;border-radius:50%;background:#999}
.dots span:first-child{background:#555}
.hero-art{position:absolute;left:780px;top:60px;width:275px;height:270px;background:radial-gradient(ellipse at 55% 55%,#6f6f6f 0%,#b9b9b9 45%,rgba(230,230,230,0) 72%)}
.main{position:absolute;left:88px;top:450px;width:994px;height:630px;background:#fff;border:1px solid var(--line)}
.main h2{font-family:"Exo 2",sans-serif;font-weight:600;font-size:23px;color:var(--heading);position:absolute}
.product{position:absolute;left:24px;width:227px}
.product .photo{width:227px;height:139px;border:1px solid #ddd}
.product h3{font-weight:400;font-size:16px;color:var(--blue);margin:13px 0 4px 15px}
.product p{font-size:12.5px;line-height:20px;color:#555;margin-left:15px}
.product .btn{margin:8px 0 0 15px;font-size:14.5px;height:32px;line-height:30px;padding:0 10px}
.lead{position:absolute;left:287px;top:64px;width:406px;font-size:16px;line-height:26.5px;color:var(--text-dark)}
.body-copy{position:absolute;left:287px;top:150px;width:406px;font-size:13.5px;line-height:24.4px;color:#555;text-align:justify}
.video{position:absolute;left:288px;top:352px;width:405px;height:245px;border-radius:4px;overflow:hidden;background:radial-gradient(ellipse at 50% 40%,#6e7058 0%,#3c3f34 55%,#1d1f1b 100%)}
.play{position:absolute;left:50%;top:44%;transform:translate(-50%,-50%)}
.controls{position:absolute;left:0;bottom:0;width:100%;height:27px;background:linear-gradient(#2a2a2a,#111)}
.controls .track{position:absolute;left:4px;top:-4px;width:397px;height:4px;background:#444}
.news{position:absolute;left:712px;width:240px;padding-left:20px}
.news::before{content:"";position:absolute;left:2px;top:5px;border-left:7px solid #777;border-top:5px solid transparent;border-bottom:5px solid transparent}
.news p{font-size:13.5px;line-height:20px;color:#444}
.news time{font-size:12.5px;color:var(--muted)}
.testimonial{position:absolute;left:727px;top:364px;width:231px;height:187px;border:1px solid #ccc;background:radial-gradient(ellipse at 55% 45%,#7a6352 0%,#2a2420 55%,#0c0c0c 100%)}
.testimonial .play{top:50%}
.client{position:absolute;left:728px;top:563px;font-size:14px;color:#222}
.client span{color:var(--muted)}
.footer-nav{position:absolute;left:87px;top:1110px;font-size:14px;color:#555;display:flex}
.footer-nav a{color:#555;text-decoration:none}
.footer-nav i{font-style:normal;padding:0 10px}
.copyright{position:absolute;left:87px;top:1144px;font-size:14px;color:#555;word-spacing:3px}
.badge{position:absolute;left:992px;top:1113px;width:89px;height:45px;border-radius:4px;background:#3a3a3a}
.badge::after{content:"";position:absolute;right:8px;top:12px;width:22px;height:22px;border-radius:3px;background:#e6b21e}
</style>
</head>
<body>
<header class="topbar">
  <div class="search">Search
    <svg width="16" height="16" viewBox="0 0 16 16"><circle cx="6.5" cy="6.5" r="5" fill="none" stroke="#fff" stroke-width="2"/><line x1="10" y1="10" x2="15" y2="15" stroke="#fff" stroke-width="2.4"/></svg>
  </div>
  <div class="brand">KelterLimb</div>
  <div class="cart">
    <svg width="24" height="19" viewBox="0 0 24 19"><path d="M1 2h4l3 10h11l3-7H7" fill="none" stroke="#2f6196" stroke-width="2"/><circle cx="10" cy="16" r="2" fill="#2f6196"/><circle cx="17" cy="16" r="2" fill="#2f6196"/></svg>
    My Cart
  </div>
  <div class="social" style="left:1011px" role="img" aria-label="Social profile link"></div>
  <div class="social" style="left:1051px" role="img" aria-label="Social profile link"></div>
</header>

<section class="hero">
  <h1>Welcome to KelterLimb</h1>
  <p>Pellentesque lacinia nunc id scelerisque molestie. Aliquam sem sapien, eleifend molestie lectus et, bibendum gravida lacus. Phasellus laoreet tincidunt ligula vel cursus. Vestibulum ante ipsum primis in faucibus orci luctus et ultrices posuere cubilia Curae; Etiam faucibus imperdiet nisl eget tempus.</p>
  <a class="btn">Order Now
    <svg width="20" height="20" viewBox="0 0 20 20"><rect width="20" height="20" fill="#fff"/><path d="M8 5l5 5-5 5" fill="none" stroke="#333" stroke-width="2"/></svg>
  </a>
  <div class="dots"><span></span><span></span><span></span><span></span></div>
  <div class="hero-art" role="img" aria-label="Robotic arm beside a human hand"></div>
</section>

<nav class="nav">
  <a class="active">Home</a><a>About Us</a><a>Investors Page</a><a>Prosthetic Hand</a><a>Robotic Hand Kits</a><a>Glove Kits</a><a>Contact Us</a>
</nav>

<main class="main">
  <h2 style="left:23px;top:20px">Our Products</h2>
  <div class="product" style="top:59px">
    <div class="photo" role="img" aria-label="Hand wearing a sensor glove" style="background:linear-gradient(135deg,#e9ecf5 0%,#b7bfdc 55%,#5a64a8 100%)"></div>
    <h3>Sensor Glove Kit</h3>
    <p>Praesent mauris bibendum fauci bus acetelit agittis ligula eu.</p>
    <a class="btn">Order Now</a>
  </div>
  <div class="product" style="top:340px">
    <div class="photo" role="img" aria-label="Robotic arm kit fitted on a hand" style="background:linear-gradient(135deg,#f3e9e6 0%,#e0b8ad 50%,#efefef 100%)"></div>
    <h3>A Robotic Arm kit</h3>
    <p>Praesent mauris bibendum fauci bus acetelit agittis ligula eu.</p>
    <a class="btn">Order Now</a>
  </div>

  <h2 style="left:287px;top:20px">How it works</h2>
  <p class="lead">Pellentesque lacinia nunc id scelerisque molestie. Aliquam sem sapien, eleifend molestie lectus et, bibendum gravida lacus. Phasellus laoreet tincidunt ligula vel cursus.</p>
  <p class="body-copy">Vestibulum ante ipsum primis in faucibus orci luctus et ultrices posuere cubilia Curae; Etiam faucibus imperdiet nisl eget tempus.Nunc rutrum aliquet orci, non aliquam dolor rutrum non. Vivamus ac consectetur ligula. Praesent eget eleifend libero. Aenean at tincidunt enim, a ornare leo. Maecenas ut urna ut sapien cursus eleifend. Vestibulum condimentum ultrices scelerisque. In hac habitasse platea dictumst. Suspendisse molestie mattis ipsum nec sodales.</p>
  <div class="video" role="img" aria-label="Video: robotic hand reaching toward a human hand">
    <svg class="play" width="92" height="92" viewBox="0 0 92 92"><circle cx="46" cy="46" r="41" fill="none" stroke="#fff" stroke-width="7"/><path d="M36 26v40l31-20z" fill="#fff"/></svg>
    <div class="controls"><div class="track"></div></div>
  </div>

  <h2 style="left:712px;top:20px">Latest News</h2>
  <div class="news" style="top:61px"><p>Phasellus laoreet tincidunt ligula rsus vestibulum ante ipsum primis</p><time>August-28-2013</time></div>
  <div class="news" style="top:142px"><p>Phasellus laoreet tincidunt ligula rsus vestibulum ante ipsum primis</p><time>August-28-2013</time></div>
  <div class="news" style="top:223px"><p>Phasellus laoreet tincidunt ligula rsus vestibulum ante ipsum primis</p><time>August-28-2013</time></div>

  <h2 style="left:712px;top:314px">Testimonials</h2>
  <div class="testimonial" role="img" aria-label="Video: client testimonial">
    <svg class="play" width="68" height="68" viewBox="0 0 68 68"><circle cx="34" cy="34" r="30" fill="none" stroke="#fff" stroke-width="5"/><path d="M27 20v28l22-14z" fill="#fff"/></svg>
  </div>
  <p class="client">Client Name, <span>3 months ago</span></p>
</main>

<footer>
  <div class="footer-nav"><a>Home</a><i>|</i><a>About us</a><i>|</i><a>Investors Page</a><i>|</i><a>Prosthetic Hand</a><i>|</i><a>Robotic Hand Kits</a><i>|</i><a>Glove Kits</a><i>|</i><a>Contact Us</a></div>
  <p class="copyright">Copyright © 2013 KelterLimb. All rights reserved.</p>
  <div class="badge" role="img" aria-label="Secure checkout badge"></div>
</footer>
</body>
</html>
```